Talbern Learning Recruitment Business Cards

We need business cards designed for our growing recruitment business.
We have just launched our offices in Sydney Melbourne and have a well established business in Perth. We are a fun young firm that specialise in Early Years Education Recruitment.
Our vision mission values are below
Our Vision:
To be:
the single, nationally recognised leader in the Early Childhood Sector.
a multifaceted organisation with a network of expertly driven facilities in the Early Childhood Sector, acknowledged as an organisation of integrity, innovation, heart and community.

Our Mission:
To provide superior quality recruitment services and solutions to the Early Childhood sector.
We empower our candidates to succeed.
We engage in trusted partnerships with our clients.
We grow our business/network/community, with passion and integrity.

Our Values:

We… are REAL
think: CUSTOMER
find: SOLUTIONS
achieve: RESULTS
enjoy: WHAT WE DO

Our website is www.talbernlearning.com feel free to visit it for inspiration.
Name Felix Ormsby
Title National Director
1300 057 812
0462 315 706
felix@talbernstaffing.com
website www.talbernlearning.com

I have attached our current business cards and logo designs to view

Target Market(s)

Recruitment

Industry/Entity Type

Business

Contact Information for Business Card

Name Felix Ormsby
Title National Director
1300 057 812
0462 315 706

Font styles to use
Serif

Requirements
Must have
• Company Values and the cities we have offices in Perth | Sydney | Melbourne
Nice to have
• Our Vision on the card
• Our Vision:
• To be a nationally recognised leader in the Early Childhood Sector.
• A multifaceted organisation with a network of expertly driven facilities in the Early Childhood Sector, acknowledged as an organisation of integrity, innovation, heart and community.

```html
<!DOCTYPE html>
<html lang="en">
<head>
<meta charset="utf-8">
<title>Talbern Learning Recruitment – Business Cards</title>
<link rel="stylesheet" href="https://fonts.googleapis.com/css2?family=Montserrat:wght@400;500;600&family=Open+Sans:wght@400;700&display=swap">
<style>
  :root {
    --bg: #eeeeec;
    --blue-light: #c4e3f8;
    --blue-mid: #4b92d6;
    --blue-deep: #1c64ae;
    --blue-text: #1f6cbd;
    --navy: #184f7c;
    --sky: #17a1e0;
    --sky-pale: #aedcf6;
    --ink: #1e1e1e;
    --grey: #4d4d4d;
    --map: #eef2fa;
    --white: #ffffff;
  }
  * { box-sizing: border-box; margin: 0; padding: 0; }
  html, body { width: 1200px; height: 872px; overflow: hidden; }
  body {
    background: var(--bg);
    position: relative;
    font-family: "Open Sans", Arial, sans-serif;
  }
  .card {
    position: absolute;
    width: 540px;
    height: 320px;
    border-radius: 16px;
    overflow: hidden;
    box-shadow: 0 10px 26px rgba(0,0,0,.14);
  }

  /* Front */
  .card-front {
    left: 40px; top: 110px;
    background: linear-gradient(180deg, var(--blue-light) 0%, var(--blue-mid) 45%, var(--blue-deep) 100%);
  }
  .front-mark {
    position: absolute;
    left: 50px; top: 108px;
    width: 124px; height: 124px;
    border: 3px solid var(--navy);
    border-radius: 50%;
  }
  .front-name {
    position: absolute;
    left: 192px; top: 134px;
    font-family: "Montserrat", Arial, sans-serif;
    font-weight: 500;
    font-size: 28px;
    letter-spacing: 1px;
    color: var(--navy);
    white-space: nowrap;
  }
  .front-tagline {
    position: absolute;
    left: 194px; top: 178px;
    font-family: "Montserrat", Arial, sans-serif;
    font-weight: 500;
    font-size: 14px;
    color: var(--navy);
    white-space: nowrap;
  }
  .front-tagline span { color: var(--sky-pale); }

  /* Back */
  .card-back {
    left: 620px; top: 440px;
    background: var(--white);
  }
  .map-area {
    position: absolute;
    left: 200px; top: 70px;
    width: 280px; height: 240px;
    border-radius: 40% 45% 35% 50%;
    background: var(--map);
  }
  .back-mark {
    position: absolute;
    left: 28px; top: 26px;
    width: 62px; height: 62px;
    border: 2px solid var(--blue-text);
    border-radius: 50%;
  }
  .back-name {
    position: absolute;
    left: 98px; top: 44px;
    font-family: "Montserrat", Arial, sans-serif;
    font-weight: 600;
    font-size: 14px;
    line-height: 1.2;
    color: var(--navy);
    letter-spacing: .5px;
  }
  .back-tagline {
    position: absolute;
    left: 26px; top: 98px;
    font-family: "Montserrat", Arial, sans-serif;
    font-weight: 600;
    font-size: 8.5px;
    color: var(--navy);
    white-space: nowrap;
  }
  .back-tagline span { color: var(--sky); }

  .offices { position: absolute; left: 0; top: 196px; list-style: none; }
  .office {
    width: 110px; height: 24px;
    margin-bottom: 10px;
    padding-left: 34px;
    background: var(--sky);
    border-radius: 0 12px 12px 0;
    color: var(--white);
    font-size: 13px;
    line-height: 24px;
  }

  .person { position: absolute; right: 78px; top: 108px; text-align: right; }
  .person-name { font-weight: 700; font-size: 26px; color: var(--blue-text); line-height: 1.1; }
  .person-title { font-size: 15px; color: var(--grey); margin-right: 30px; }

  .contacts {
    position: absolute; right: 78px; top: 212px;
    text-align: right; color: var(--ink); font-size: 15px; line-height: 1.25;
  }
  .contacts .email { margin-top: 8px; }
  .contacts .web { margin-top: 10px; }

  .side-bar {
    position: absolute; right: 10px; top: 0;
    width: 34px; height: 320px;
    border-radius: 0 0 10px 10px;
    background: linear-gradient(180deg, var(--blue-light) 0%, var(--blue-mid) 55%, var(--blue-deep) 100%);
  }
  .icon {
    position: absolute; left: 5px;
    width: 24px; height: 24px;
    border-radius: 50%;
    background: var(--white);
    display: flex; align-items: center; justify-content: center;
  }
  .icon svg { width: 14px; height: 14px; fill: none; stroke: var(--blue-deep); stroke-width: 2; }
</style>
</head>
<body>

  <section class="card card-front" aria-label="Business card front">
    <div class="front-mark"></div>
    <div class="front-name">TALBERN LEARNING</div>
    <div class="front-tagline">Placing passionate people <span>in early learning</span></div>
  </section>

  <section class="card card-back" aria-label="Business card back">
    <div class="map-area" role="img" aria-label="Faint map of Australia with office locations"></div>

    <div class="back-mark"></div>
    <div class="back-name">TALBERN<br>LEARNING</div>
    <div class="back-tagline">Placing passionate people <span>in early learning</span></div>

    <ul class="offices">
      <li class="office">Perth</li>
      <li class="office">Sydney</li>
      <li class="office">Melbourne</li>
    </ul>

    <div class="person">
      <div class="person-name">Felix Ormsby</div>
      <div class="person-title">National Director</div>
    </div>

    <div class="contacts">
      <div>1300 057 812</div>
      <div>0462 315 706</div>
      <div class="email">felix@talbernstaffing.com</div>
      <div class="web">www.talbernlearning.com</div>
    </div>

    <div class="side-bar">
      <span class="icon" style="top:214px" aria-label="Phone">
        <svg viewBox="0 0 24 24"><path d="M6 3l3 4-2 2c1 3 4 6 7 7l2-2 4 3-2 4C10 21 3 14 2 5z"/></svg>
      </span>
      <span class="icon" style="top:250px" aria-label="Email">
        <svg viewBox="0 0 24 24"><rect x="3" y="6" width="18" height="12"/><path d="M3 6l9 7 9-7"/></svg>
      </span>
      <span class="icon" style="top:286px" aria-label="Website">
        <svg viewBox="0 0 24 24"><circle cx="12" cy="12" r="9"/><ellipse cx="12" cy="12" rx="4" ry="9"/><path d="M3 12h18M5 7h14M5 17h14"/></svg>
      </span>
    </div>
  </section>

</body>
</html>
```